iOS App Design Project for Pebble Tasks

We are looking for a redesign of the UI for our app, Pebble Tasks. The app is a to-do list type app with 4 screens, and we already have a UI for it but we would like a nicer looking one that has a better colour scheme and is more intuitive.

We would like something that is a real treat to look at, and that users really want to use. Essentially what we want is the nicest and most simple design possible, as the current UI we have is not very user friendly.

The app is already on the market and is free so if you have an iOS device you can download it and take a look at it, and we have also included screenshots of the app.
Updates

Project Deadline Extended
Reason: I am updating the design brief and will also guarantee the payment.

Target Market(s)

Mobile users looking for simplicity

Requirements
Must have
• - Very visually pleasing
- Simple layout with minimal clutter
- Icons and buttons that explain what they do
Should not have
• Any features that detract from the simplicity of the app are not wanted.

```html
<!DOCTYPE html>
<html lang="en">
<head>
<meta charset="utf-8">
<title>Notes</title>
<link rel="stylesheet" href="https://fonts.googleapis.com/css2?family=Open+Sans:wght@700&display=swap">
<style>
  :root {
    --canvas: #e3e2e2;
    --bar-top: #74adc3;
    --bar-bottom: #3b6a8d;
    --tab-active: #2f4f66;
    --board: #4a4542;
    --paper-top: #e1e3e0;
    --paper-bottom: #a8ada9;
    --rule: #6a6d6b;
    --rule-red: #d0736a;
    --margin-blue: #7f97c4;
    --icon: #eef3f6;
  }
  html, body {
    margin: 0;
    width: 1200px;
    height: 1000px;
    overflow: hidden;
    background: var(--canvas);
  }
  .app-screen {
    position: absolute;
    left: 21px;
    top: 20px;
    width: 639px;
    height: 960px;
    background: var(--board);
    overflow: hidden;
  }
  .title-bar {
    position: absolute;
    left: 0; top: 0;
    width: 100%;
    height: 88px;
    background: linear-gradient(var(--bar-top), var(--bar-bottom));
  }
  .title-bar h1 {
    position: absolute;
    left: 0;
    width: 612px;
    top: 0;
    line-height: 92px;
    text-align: center;
    margin: 0;
    font: 700 41px "Open Sans", sans-serif;
    color: #e4e9ec;
    letter-spacing: 0.3px;
    text-shadow: 0 -1px 0 rgba(0,0,0,0.35), 0 1px 1px rgba(255,255,255,0.2);
  }
  .note-sheet {
    position: absolute;
    left: 0; top: 88px;
  }
  .tab-bar {
    position: absolute;
    left: 0; bottom: 0;
    width: 100%;
    height: 90px;
    background: linear-gradient(var(--bar-top), var(--bar-bottom));
    border-top: 1px solid #2e3a44;
  }
  .tab-bar svg { display: block; }
</style>
</head>
<body>
<main class="app-screen">
  <header class="title-bar"><h1>NOTES</h1></header>

  <svg class="note-sheet" width="639" height="760" viewBox="0 0 639 760" aria-hidden="true">
    <defs>
      <linearGradient id="paperFill" x1="0" y1="0" x2="0" y2="1">
        <stop offset="0" stop-color="var(--paper-top)"/>
        <stop offset="1" stop-color="var(--paper-bottom)"/>
      </linearGradient>
      <filter id="sheetShadow" x="-5%" y="-5%" width="110%" height="115%">
        <feGaussianBlur stdDeviation="4"/>
      </filter>
      <path id="sheetShape"
        d="M0 0 H616 V712
           a14 14 0 0 0 -28 0 a14 14 0 0 0 -28 0 a14 14 0 0 0 -28 0 a14 14 0 0 0 -28 0
           a14 14 0 0 0 -28 0 a14 14 0 0 0 -28 0 a14 14 0 0 0 -28 0 a14 14 0 0 0 -28 0
           a14 14 0 0 0 -28 0 a14 14 0 0 0 -28 0 a14 14 0 0 0 -28 0 a14 14 0 0 0 -28 0
           a14 14 0 0 0 -28 0 a14 14 0 0 0 -28 0 a14 14 0 0 0 -28 0 a14 14 0 0 0 -28 0
           a14 14 0 0 0 -28 0 a14 14 0 0 0 -28 0 a14 14 0 0 0 -28 0 a14 14 0 0 0 -28 0
           a14 14 0 0 0 -28 0 a14 14 0 0 0 -28 0 Z"/>
    </defs>
    <g transform="translate(12,0)">
      <use href="#sheetShape" filter="url(#sheetShadow)" fill="rgba(0,0,0,0.6)" transform="translate(0,9)"/>
      <use href="#sheetShape" fill="url(#paperFill)"/>
      <line x1="4" y1="17" x2="612" y2="17" stroke="#8d908e" stroke-width="3" stroke-dasharray="20 9"/>
      <line x1="8" y1="103" x2="607" y2="103" stroke="var(--rule-red)" stroke-width="2"/>
      <g stroke="var(--rule)" stroke-width="2">
        <line x1="8" y1="174" x2="607" y2="174"/>
        <line x1="8" y1="245" x2="607" y2="245"/>
        <line x1="8" y1="317" x2="607" y2="317"/>
        <line x1="8" y1="388" x2="607" y2="388"/>
        <line x1="8" y1="462" x2="607" y2="462"/>
        <line x1="8" y1="533" x2="607" y2="533"/>
        <line x1="8" y1="606" x2="607" y2="606"/>
      </g>
      <line x1="24" y1="35" x2="24" y2="682" stroke="var(--margin-blue)" stroke-width="2"/>
    </g>
  </svg>

  <nav class="tab-bar" aria-label="Sections">
    <svg width="639" height="90" viewBox="0 0 639 90">
      <g fill="none" stroke="var(--icon)" stroke-width="2.5">
        <rect x="21" y="17" width="58" height="58"/>
        <g fill="var(--icon)" stroke="none">
          <rect x="30" y="29" width="40" height="6"/>
          <rect x="30" y="40" width="40" height="6"/>
          <rect x="30" y="51" width="40" height="6"/>
          <rect x="30" y="62" width="40" height="5"/>
        </g>
        <rect x="202" y="16" width="58" height="58"/>
        <path d="M214 46 L226 58 L249 33" stroke-width="6" stroke-linecap="round" stroke-linejoin="round"/>
      </g>
      <rect x="372" y="0" width="95" height="90" fill="var(--tab-active)" opacity="0.75"/>
      <g fill="none" stroke="var(--icon)" stroke-width="2.5">
        <path d="M416 20 H396 V74 H440 V50"/>
        <path d="M400 14 V24 M407 14 V24 M414 14 V24 M421 14 V24 M428 14 V24 M435 14 V24" stroke-width="2"/>
        <path d="M396 20 H440 V30"/>
        <path d="M423 64 L447 36 L453 42 L429 70 L420 72 Z"/>
      </g>
      <path d="M575 22 H589 V38 H606 V52 H589 V69 H575 V52 H558 V38 H575 Z" fill="var(--icon)"/>
    </svg>
  </nav>
</main>
</body>
</html>
```